Label and logo design for an all natural organic skincare product

We need a label design for a new company in the natural beauty space. The company is called "Vessa Kell". "Vessa" refers to the olive tree. "Kell" symbolizes the wren bird. The company name represents purity, nature, and freedom.

Our first product is tamanu oil - a 100% pure, organic, unrefined, cold pressed oil that is be used to improve various skin conditions (acne, eczema, scars, anti-aging) hair, and nails. Tamanu oil is a wonderful skin care healing agent that fades scars, rejuvenates skin cells, and is a powerful natural anti-aging product.

We currently do not have a company logo. We would like the logo and label to be designed together for a coordinated, well thought out, look.

We are looking for a label and logo that convey a high end quality product. We use premium quality all natural ingredients only.

Label size is 10.2cm (wide) x 4.5cm (height). The label wraps around a small amber colored glass bottle with a dropper similar to the images attached. The bottle holds 1oz (30ml) of oil.

Label will contain:
- Company logo
- Product name - "100% Pure Organic Tamanu Oil"
- Quantity - "1 fl oz / 30 ml"
- Ingredients - "100% pure virgin organic cold pressed tamanu oil (calophyllum inophyllum)
- Product Usage - "Dab a few drops of Vessa Kell tamanu oil into your hands and rub the oil into your skin or hair 1 - 3 times a day."
- UPC barcode - will provide later
- Company info:
"Vessa Kell
Brenmoor Bay
www.vessakell.example"
- Warning - "For external use only. Do not use if you have allergies to nuts of any kind. Keep out of reach of children."

We've attached a couple images of labels that we like. In general, we prefer a modern, minimalistic, pure look but we are open to your ideas and creativity.

Colors we like: blue-green (think torquoise or tiffany blue), green, grey, white.

If you have any questions, about the design please let me know. The winning designer will be required to do a few additional tweaks to finalize the product. Thank you for your time and happy designing!

```html
<!DOCTYPE html>
<html lang="en">
<head>
<meta charset="utf-8">
<title>Vessa Kell – Tamanu Oil Label</title>
<link rel="stylesheet" href="https://fonts.googleapis.com/css2?family=Mulish:ital,wght@0,400;0,600;0,700;0,800;1,400;1,600&display=swap">
<style>
  :root {
    --sky-white: #ffffff;
    --sky-pale: #d6f1fb;
    --aqua: #39bde6;
    --aqua-deep: #0fa2d6;
    --teal-edge: #1a9dbd;
    --brand-blue: #1f5fb0;
    --title-red: #e2401c;
    --ingredient-indigo: #2e2f8a;
    --ink: #1b2228;
  }
  * { margin: 0; padding: 0; box-sizing: border-box; }
  html, body {
    width: 1200px;
    height: 526px;
    overflow: hidden;
    background: var(--sky-white);
  }
  .label {
    position: relative;
    width: 1200px;
    height: 526px;
    overflow: hidden;
    font-family: "Mulish", "Century Gothic", sans-serif;
    color: var(--ink);
    background:
      radial-gradient(ellipse 520px 170px at 600px 40px, var(--sky-white) 0%, rgba(255,255,255,0.85) 35%, rgba(255,255,255,0) 100%),
      radial-gradient(ellipse 900px 420px at 560px 130px, var(--sky-pale) 0%, rgba(214,241,251,0) 70%),
      linear-gradient(180deg, #bfe9f8 0%, var(--aqua) 55%, var(--aqua-deep) 100%);
  }
  .label::after {
    content: "";
    position: absolute;
    inset: 0;
    background: radial-gradient(ellipse 380px 300px at 1200px 180px, rgba(26,157,189,0.55), rgba(26,157,189,0));
    pointer-events: none;
  }
  .wave-texture {
    position: absolute;
    inset: 0;
    background: radial-gradient(ellipse 700px 120px at 450px 300px, rgba(255,255,255,0.22), rgba(255,255,255,0) 100%);
  }
  .content { position: relative; z-index: 1; width: 100%; height: 100%; }
  .brand-name {
    position: absolute;
    top: 40px;
    left: 0;
    width: 100%;
    text-align: center;
    font-size: 66px;
    font-weight: 800;
    letter-spacing: 1px;
    color: var(--brand-blue);
  }
  .product-name {
    position: absolute;
    top: 179px;
    left: 0;
    width: 100%;
    text-align: center;
    font-size: 31px;
    font-weight: 700;
    letter-spacing: 0.9px;
    color: var(--title-red);
  }
  .ingredients {
    position: absolute;
    top: 236px;
    left: 0;
    width: 100%;
    text-align: center;
    font-size: 23px;
    font-style: italic;
    font-weight: 600;
    letter-spacing: 0.9px;
    line-height: 30px;
    color: var(--ingredient-indigo);
  }
  .quantity {
    position: absolute;
    top: 376px;
    left: 56px;
    font-size: 25px;
    font-weight: 700;
    letter-spacing: 1.6px;
  }
  .company-info {
    position: absolute;
    top: 334px;
    left: 914px;
    font-size: 22px;
    font-style: normal;
    letter-spacing: 0.8px;
    line-height: 27px;
  }
  .company-info strong {
    display: block;
    font-size: 25px;
    font-weight: 700;
    letter-spacing: 0.6px;
    line-height: 30px;
  }
  .usage-notes {
    position: absolute;
    top: 441px;
    left: 56px;
    width: 1130px;
    font-size: 17.5px;
    font-style: italic;
    letter-spacing: 0.75px;
    line-height: 25px;
    white-space: nowrap;
  }
</style>
</head>
<body>
  <main class="label">
    <div class="wave-texture" role="img" aria-label="Soft flowing line pattern sweeping across the label"></div>
    <div class="content">
      <h1 class="brand-name">Vessa Kell</h1>
      <h2 class="product-name">100% Pure Organic Tamanu Oil</h2>
      <p class="ingredients">100% pure virgin organic<br>cold pressed tamanu oil<br>(calophyllum inophyllum)</p>
      <p class="quantity">1 fl oz / 30 ml</p>
      <address class="company-info">
        <strong>Vessa Kell</strong>
        Brenmoor Bay<br>
        www.vessakell.example
      </address>
      <p class="usage-notes">
        Dab a few drops of Vessa Kell tamanu oil into your hands and rub the oil into your skin or hair 1 - 3 times a day.<br>
        Warning: For external use only. Do not use if you have allergies to nuts of any kind. Keep out of reach of children.
      </p>
    </div>
  </main>
</body>
</html>
```